Website for Tech Venture Capital - Trovik Capital

We need a website for Trovik Capital.
Slogan:
Helping Ambitious Entrepreneurs Start and Build Great Companies.

Trovik Capital is a venture capital looking to support and invest in young talent within the technology and digital marketing industry. We wish for a website that reflects that while matching our logo and color palette.

Our Domain is: https://trovik.vc/
We would like to have these considered as references/inspiration for our website:
https://www.bluntmoorfund.com/
https://www.quendalpartners.com/israel/

You can find the desired structure and the zip file attached.
There is a color palette attached as well.
Social media pages to be used:
https://www.linkedin.com/in/doronmatsbai/
https://www.linkedin.com/in/nimrod-tal-ezra/
https://www.linkedin.com/in/kovner/

Target Market(s)

Young Tech and Digital Marketing Entrepreneurs

Industry/Entity Type

Tech, Finance

Coding

Coded - Design and coding required

Number of Pages Required

4 page

Font styles to use
Sans Serif

Colors
0054AA
0677BA
7BADD7
CADEEF
E8F1F8
0094D4
00A9DD
6FCCEA
C7EBF8
E9F6FB

Requirements
Must have
• Please see attached files. WordPress sites strongly preferred.

```html
<!DOCTYPE html>
<html lang="en">
<head>
<meta charset="utf-8">
<title>Trovik Capital</title>
<link href="https://fonts.googleapis.com/css2?family=Playfair+Display:wght@400;700&family=Lato:wght@400;700&display=swap" rel="stylesheet">
<style>
:root{
  --navy:#121f55;
  --navy-deep:#0d1846;
  --blue:#0094d4;
  --cyan:#00a9dd;
  --sky:#c7ebf8;
  --ink:#1d2433;
  --muted:#6b7384;
  --soft:#f4f6f9;
  --white:#ffffff;
  --serif:'Playfair Display', Georgia, serif;
  --sans:'Lato', Arial, sans-serif;
}
*{box-sizing:border-box;margin:0;padding:0}
html,body{width:1200px;height:2780px;overflow:hidden}
body{font-family:var(--sans);color:var(--ink);background:var(--white)}
.wrap{width:1000px;margin:0 auto}
.topbar{height:28px;background:var(--navy-deep);color:#b8c2dc;font-size:12px}
.topbar .wrap{display:flex;align-items:center;height:28px;gap:8px}
.topbar .dot{width:8px;height:8px;background:var(--cyan)}
.header{height:72px;background:var(--navy)}
.header .wrap{display:flex;align-items:center;justify-content:space-between;height:72px}
.brand{display:flex;align-items:center;gap:10px;color:var(--white);font-family:var(--serif);font-weight:700;font-size:24px;letter-spacing:1px}
.brand-square{width:14px;height:14px;background:var(--cyan)}
.nav{display:flex;gap:36px;list-style:none;font-size:14px;color:var(--white)}
.nav li.active{color:var(--cyan)}
.hero{position:relative;height:620px}
.hero-photo{position:absolute;inset:0;background:linear-gradient(135deg,#3d5a80 0%,#27406b 45%,#1a2c52 100%)}
.hero-shade{position:absolute;inset:0;background:linear-gradient(90deg,rgba(13,24,70,.75),rgba(13,24,70,.25))}
.hero-content{position:relative;padding-top:190px}
.eyebrow{font-size:12px;letter-spacing:3px;text-transform:uppercase}
.hero .eyebrow{color:var(--sky)}
.hero h1{font-family:var(--serif);font-weight:700;color:var(--white);font-size:46px;line-height:1.2;max-width:620px;margin:18px 0 36px}
.btn{display:inline-block;background:var(--cyan);color:var(--white);font-size:14px;font-weight:700;padding:14px 28px}
.about{padding:110px 0;height:560px}
.about .wrap{display:flex;justify-content:space-between;align-items:center}
.about-text{width:520px}
.about .eyebrow,.team .eyebrow,.contact .eyebrow{color:var(--muted)}
.section-title{font-family:var(--serif);font-weight:700;color:var(--navy);font-size:40px;margin:14px 0 26px}
.about p{font-size:14px;line-height:1.8;color:var(--muted);margin-bottom:14px}
.about p strong{color:var(--navy)}
.about-mark{width:300px;height:300px;background:var(--navy);margin-right:60px}
.team{background:var(--soft);padding:90px 0;height:620px;text-align:center}
.cards{display:flex;justify-content:center;gap:30px;margin-top:20px}
.card{width:280px;background:var(--white);box-shadow:0 4px 14px rgba(18,31,85,.08)}
.card-photo{height:230px;background:linear-gradient(180deg,#e4e7ec,#c9ced7)}
.card-body{padding:18px 0 22px}
.card-name{font-family:var(--serif);font-weight:700;color:var(--navy);font-size:18px}
.card-role{font-size:13px;color:var(--muted);margin:6px 0 12px}
.card-link{display:inline-block;width:22px;height:22px;background:var(--blue)}
.contact{padding:90px 0;height:440px}
.contact .wrap{display:flex;justify-content:space-between}
.contact-lead{width:520px}
.contact-lead .section-title{font-size:36px;line-height:1.3}
.offices{width:300px;padding-top:40px}
.office{margin-bottom:30px}
.office h3{font-family:var(--serif);color:var(--navy);font-size:18px;margin-bottom:8px}
.office p{font-size:13px;color:var(--muted);line-height:1.6}
.footer{background:var(--navy);color:#c2cadf;height:520px;padding-top:80px}
.footer-grid{display:flex;justify-content:space-between}
.footer-about{width:420px}
.footer-about p{font-size:13px;line-height:1.8;margin-top:24px}
.links h4{font-family:var(--serif);color:var(--white);font-size:20px;font-weight:400;margin-bottom:20px}
.links ul{list-style:none;font-size:13px;line-height:2.2}
.links-group{display:flex;gap:110px;margin-right:40px}
.copyright{margin-top:120px;border-top:1px solid rgba(255,255,255,.15);padding-top:26px;text-align:center;font-size:12px}
</style>
</head>
<body>
<div class="topbar"><div class="wrap"><span class="dot"></span>info@trovik.vc</div></div>
<header class="header">
  <div class="wrap">
    <div class="brand"><span class="brand-square"></span>Trovik Capital</div>
    <ul class="nav"><li class="active">Home</li><li>About</li><li>Team</li><li>Contact</li></ul>
  </div>
</header>

<section class="hero">
  <div class="hero-photo" role="img" aria-label="Photo of a team working together at a table"></div>
  <div class="hero-shade"></div>
  <div class="wrap hero-content">
    <div class="eyebrow">Backing founders in tech and digital marketing</div>
    <h1>Helping Ambitious Entrepreneurs Start and Build Great Companies</h1>
    <span class="btn">Contact Us</span>
  </div>
</section>

<section class="about">
  <div class="wrap">
    <div class="about-text">
      <div class="eyebrow">Introducing</div>
      <h2 class="section-title">About Trovik Capital</h2>
      <p><strong>Trovik Capital</strong> is an early-stage venture firm backing founders in technology and digital marketing. We partner with ambitious teams from the first idea to the first real scale.</p>
      <p>We bring capital, hands-on guidance and a trusted network so founders can focus on product, customers and growth. Our partners have built, run and sold companies of their own.</p>
      <p>We invest where we can truly help, and we stay close long after the first cheque.</p>
    </div>
    <div class="about-mark" aria-hidden="true"></div>
  </div>
</section>

<section class="team">
  <div class="wrap">
    <div class="eyebrow">Meet</div>
    <h2 class="section-title">Our Team</h2>
    <div class="cards">
      <div class="card"><div class="card-photo" role="img" aria-label="Portrait of Doron Matsbai"></div><div class="card-body"><div class="card-name">Doron Matsbai</div><div class="card-role">Managing Partner</div><span class="card-link"></span></div></div>
      <div class="card"><div class="card-photo" role="img" aria-label="Portrait of Nimrod Tal-Ezra"></div><div class="card-body"><div class="card-name">Nimrod Tal-Ezra</div><div class="card-role">General Partner</div><span class="card-link"></span></div></div>
      <div class="card"><div class="card-photo" role="img" aria-label="Portrait of Amit Kovner"></div><div class="card-body"><div class="card-name">Amit Kovner</div><div class="card-role">Venture Partner</div><span class="card-link"></span></div></div>
    </div>
  </div>
</section>

<section class="contact">
  <div class="wrap">
    <div class="contact-lead">
      <div class="eyebrow">Contact</div>
      <h2 class="section-title">For general inquiries,<br>you can email us at info@trovik.vc</h2>
    </div>
    <div class="offices">
      <div class="office"><h3>New York</h3><p>120 Hudson Street, New York, NY</p></div>
      <div class="office"><h3>Israel</h3><p>18 Harbour Road, Tel Aviv</p></div>
    </div>
  </div>
</section>

<footer class="footer">
  <div class="wrap">
    <div class="footer-grid">
      <div class="footer-about">
        <div class="brand"><span class="brand-square"></span>Trovik Capital</div>
        <p>Trovik Capital helps ambitious entrepreneurs start and build great companies across technology and digital marketing.</p>
      </div>
      <div class="links-group">
        <div class="links"><h4>Quick Links</h4><ul><li>Home</li><li>About</li><li>Team</li><li>Contact</li></ul></div>
        <div class="links"><h4>Quick Links</h4><ul><li>Privacy</li><li>Terms</li><li>Careers</li><li>News</li></ul></div>
      </div>
    </div>
    <div class="copyright">© 2024 Trovik Capital. All rights reserved.</div>
  </div>
</footer>
</body>
</html>
```